Website and Mobile Devices design for food related application.

We need a design that is simple yet playful. The design should be food related if possible.
This design will be on the website and the mobile platform markets we intend application to be deployed too.
This application/website is called "Bitelora[.com]. Its a random restaurant picker for the indecisive users.
Updates
Hi all, I picked a design. Again lots of great designs were submitted but I picked one that was more in line with what I wanted.
Target Market(s)
young internet savvy users.
Industry/Entity Type
Restaurant
Look and feel
Each slider illustrates characteristics of the customer's brand and the style your logo design should communicate.

```html
<!DOCTYPE html>
<html lang="en">
<head>
<meta charset="utf-8">
<title>Bitelora — Random restaurant picker</title>
<link rel="stylesheet" href="https://fonts.googleapis.com/css2?family=Arvo:ital,wght@0,400;0,700;1,400&family=Roboto+Slab:wght@300&family=Arimo:wght@400&display=swap">
<style>
  :root {
    --brand-red: #c1294b;
    --heading-blue: #3f7799;
    --ink: #1a1a1a;
    --header-bg: #ffffff;
    --picker-bg: #f5f5f5;
    --list-bg: #ebebed;
    --rim: #dedede;
    --rim-edge: #e9e9e9;
    --frame: #f4f4f2;
    --slice-blue: #3f6a8b;
    --slice-teal: #3aa595;
    --slice-green: #3dab4d;
    --slice-yellow: #e2c61b;
    --slice-orange: #f0b131;
    --slice-red: #cc3449;
  }
  * { box-sizing: border-box; margin: 0; padding: 0; }
  html, body { width: 1200px; height: 927px; overflow: hidden; background: var(--header-bg); }
  body { font-family: "Arimo", Helvetica, Arial, sans-serif; color: var(--ink); }

  .site-header {
    height: 95px;
    display: flex;
    align-items: center;
    justify-content: space-between;
    padding: 0 60px 0 63px;
  }
  .brand-name {
    font-family: "Arvo", serif;
    font-weight: 700;
    font-size: 40px;
    color: var(--brand-red);
    letter-spacing: 0.2px;
  }
  .nav-contacts {
    font-size: 21px;
    color: var(--ink);
    text-decoration: underline;
    text-underline-offset: 3px;
  }

  .app-main { display: flex; height: 832px; }

  .picker {
    width: 664px;
    background: var(--picker-bg);
    position: relative;
  }
  .picker-prompt {
    position: absolute;
    left: 63px;
    top: 62px;
    font-family: "Roboto Slab", serif;
    font-weight: 300;
    font-size: 27px;
    color: #2a2a2a;
  }
  .spin-wheel {
    position: absolute;
    left: 40px;
    top: 162px;
    width: 590px;
    height: 590px;
  }
  .spin-label {
    font-family: "Arvo", serif;
    font-style: italic;
    font-size: 26px;
    fill: #444;
  }

  .results {
    flex: 1;
    background: var(--list-bg);
    padding: 62px 60px 0 46px;
  }
  .cuisine-title {
    font-family: "Arvo", serif;
    font-weight: 700;
    font-size: 26px;
    color: var(--heading-blue);
    margin-bottom: 50px;
  }
  .restaurant-list { list-style: none; }
  .restaurant { height: 77.5px; }
  .restaurant-name { font-size: 20px; line-height: 26px; color: var(--ink); }
  .restaurant-address { font-size: 17px; line-height: 24px; color: #333; }
  .address-label { color: var(--brand-red); }
</style>
</head>
<body>
  <header class="site-header">
    <div class="brand-name">Bitelora</div>
    <a class="nav-contacts" href="#">Contacts</a>
  </header>

  <main class="app-main">
    <section class="picker">
      <h2 class="picker-prompt">Today I’m feeling....</h2>
      <svg class="spin-wheel" viewBox="-295 -295 590 590" role="img" aria-label="Spinning wheel of food categories: Chinese, burgers, sushi, desserts, pizza and drinks">
        <circle class="wheel-rim" r="278" fill="var(--rim)" stroke="var(--rim-edge)" stroke-width="4"/>
        <g class="wheel-slices">
          <path fill="var(--slice-teal)"   d="M0 0 L255 0 A255 255 0 0 0 127.5 -220.8 Z"/>
          <path fill="var(--slice-red)"    d="M0 0 L-127.5 -220.8 A255 255 0 0 0 -255 0 Z"/>
          <path fill="var(--slice-orange)" d="M0 0 L-255 0 A255 255 0 0 0 -127.5 220.8 Z"/>
          <path fill="var(--slice-yellow)" d="M0 0 L-127.5 220.8 A255 255 0 0 0 127.5 220.8 Z"/>
          <path fill="var(--slice-green)"  d="M0 0 L127.5 220.8 A255 255 0 0 0 255 0 Z"/>
        </g>
        <path class="slice-selected" fill="var(--slice-blue)" stroke="var(--frame)" stroke-width="14" stroke-linejoin="round"
              d="M0 0 L133 -230.4 A266 266 0 0 0 -133 -230.4 Z"/>
        <circle class="spin-button" r="58" fill="#f7f7f5" stroke="#dcdcdc" stroke-width="6"/>
        <text class="spin-label" x="0" y="9" text-anchor="middle">Spin!</text>
      </svg>
    </section>

    <section class="results">
      <h2 class="cuisine-title">Chinese</h2>
      <ul class="restaurant-list">
        <li class="restaurant">
          <div class="restaurant-name">Lantern House</div>
          <div class="restaurant-address"><span class="address-label">Address:</span> Carrer de l'Olivera, 112</div>
        </li>
        <li class="restaurant">
          <div class="restaurant-name">Wok &amp; Ladle</div>
          <div class="restaurant-address"><span class="address-label">Address:</span> Carrer del Taronger, 286</div>
        </li>
        <li class="restaurant">
          <div class="restaurant-name">Jade Garden</div>
          <div class="restaurant-address"><span class="address-label">Address:</span> Carrer de la Salvia, 19</div>
        </li>
        <li class="restaurant">
          <div class="restaurant-name">Bamboo Court</div>
          <div class="restaurant-address"><span class="address-label">Address:</span> Carrer de les Barques, 14</div>
        </li>
        <li class="restaurant">
          <div class="restaurant-name">Silver Peony</div>
          <div class="restaurant-address"><span class="address-label">Address:</span> Avinguda dels Til·lers Alts, 22</div>
        </li>
        <li class="restaurant">
          <div class="restaurant-name">Golden Lotus</div>
          <div class="restaurant-address"><span class="address-label">Address:</span> Carrer del Mestre Roca, 46</div>
        </li>
        <li class="restaurant">
          <div class="restaurant-name">Red Crane</div>
          <div class="restaurant-address"><span class="address-label">Address:</span> Carrer de l' Estel, 5</div>
        </li>
      </ul>
    </section>
  </main>
</body>
</html>
```